IT Consulting Firm Website
Core Values: Proficiency ♦ Consistency ♦ Integrity
IT Consulting Firm Website - Information Technology
Creative Brief
Information Technology
www.dunmorevantage.com
Premier IT Services Consulting firm with a heavy emphasis on ethical business practices and superior technical skillsets. Dunmore Consulting designs and implements effective solutions that are specific to the client's information technology issues and business model. Harness our ability to assess your information technology concerns and deliver a solution that meets the company's current requirements and plan appropriately for the company's future demands. DCHP understands how technology works and has a clear focus enabling us to accurately read the strategic big picture of any business challenge. Business continuity and disaster recovery plans are also addressed and implemented as part of the IT solution. Dunmore Consulting has led successful efforts in delivering effective IT solutions to difficult and complex business challenges.
we are looking for a website design that will establish our brand as professional, ethical and technically superior to our competitors. Nothing cartoonish. Something that will identify us by the solid and stable IT industry relationships we've developed.
Modern
Core color is Cobalt Blue (Pantone 288C - RGB 00337F)
RGB 1975FF
RGB 3F3F3F & RGB 000000
below header
Please use images from www.lumepixbank.com Also, please make sure you guys use our NEW logo that I've uploaded to the project and to design with that in mind. Not our old logo that you see on the website.

```html
<!DOCTYPE html>
<html lang="en">
<head>
<meta charset="utf-8">
<title>Dunmore Consulting Group</title>
<link rel="stylesheet" href="https://fonts.googleapis.com/css2?family=Open+Sans:wght@400;600;700&display=swap">
<style>
  :root {
    --cobalt: #00337f;
    --cobalt-dark: #002260;
    --bright-blue: #1975ff;
    --charcoal: #3f3f3f;
    --ink: #000000;
    --page: #e4e6ea;
    --white: #ffffff;
    --panel-grey: #efefef;
    --rule: #d2d4d8;
    --text: #333333;
  }
  * { box-sizing: border-box; margin: 0; padding: 0; }
  html, body { width: 1200px; height: 1060px; overflow: hidden; }
  body {
    background: var(--page);
    font-family: "Open Sans", Arial, sans-serif;
    color: var(--text);
    position: relative;
  }
  .site-header { position: absolute; left: 0; top: 0; width: 1200px; height: 137px; }
  .brand {
    position: absolute; left: 100px; top: 44px;
    display: flex; align-items: center; gap: 16px;
  }
  .brand-mark { width: 58px; height: 58px; border-radius: 50%; background: var(--cobalt); }
  .brand-name { font-size: 34px; font-weight: 600; color: var(--cobalt); letter-spacing: 0.5px; }

  .main-nav {
    position: absolute; left: 34px; top: 137px; width: 1123px; height: 50px;
    background: linear-gradient(#0d4aa3, var(--cobalt) 55%, var(--cobalt-dark));
    border-radius: 3px;
    display: flex; align-items: center; padding-left: 44px;
  }
  .main-nav a {
    color: var(--white); text-decoration: none; font-size: 15px; font-weight: 600;
    margin-right: 60px; letter-spacing: 0.3px;
  }
  .search { position: absolute; right: 28px; top: 12px; display: flex; gap: 6px; }
  .search-field {
    width: 218px; height: 27px; background: var(--white); border-radius: 2px;
    font-size: 14px; color: var(--charcoal); padding: 4px 8px;
  }
  .search-button { width: 27px; height: 27px; background: var(--white); border-radius: 2px; }

  .intro {
    position: absolute; left: 34px; top: 196px; width: 1123px; height: 200px;
    background: var(--white);
  }
  .intro-title {
    position: absolute; left: 52px; top: 38px;
    font-size: 24px; font-weight: 400; color: var(--bright-blue);
  }
  .intro-copy {
    position: absolute; left: 52px; width: 700px;
    font-size: 13.5px; line-height: 19px; color: var(--text);
  }
  .intro-lead { top: 86px; }
  .intro-detail { top: 124px; }
  .offices {
    position: absolute; left: 781px; top: 18px; width: 330px; height: 144px;
    background: var(--panel-grey); border: 1px solid var(--rule); padding: 18px 22px;
  }
  .offices-title {
    font-size: 21px; font-weight: 400; color: var(--charcoal);
    margin-bottom: 18px; white-space: nowrap;
  }
  .offices-line { font-size: 15px; line-height: 22px; color: var(--charcoal); }

  .services {
    position: absolute; left: 34px; top: 414px; width: 1123px; height: 357px;
    background: linear-gradient(#5a5a5a, var(--charcoal));
    display: flex; gap: 50px; padding: 37px 0 0 43px;
  }
  .service { width: 316px; color: var(--white); }
  .service-photo { width: 316px; height: 135px; border: 2px solid #cfcfcf; }
  .photo-network { background: linear-gradient(135deg, #f2f4f6, #a9b0b8 60%, #7b838c); }
  .photo-managed { background: linear-gradient(135deg, #3b3f44, #7d6f60 55%, #b9b0a3); }
  .photo-cloud { background: linear-gradient(#7fc8ee, #cfeaf8 55%, #ffffff); }
  .service h3 { font-size: 15px; font-weight: 700; margin: 26px 0 12px; letter-spacing: 0.2px; white-space: nowrap; }
  .service ul { list-style: none; padding-left: 48px; font-size: 13.5px; line-height: 17px; }
  .learn-more {
    display: inline-block; margin-top: 16px; padding: 2px 10px;
    background: var(--white); color: var(--bright-blue);
    font-size: 12px; font-weight: 700; border-radius: 2px; text-decoration: none;
  }

  .partners {
    position: absolute; left: 34px; top: 808px; width: 1123px; height: 100px;
    background: var(--white);
    display: flex; align-items: center; justify-content: space-around; padding: 0 40px;
  }
  .partner { background: #9aa0a8; }
  .partner-wide { width: 118px; height: 32px; border-radius: 3px; }
  .partner-round { width: 56px; height: 56px; border-radius: 50%; background: #b07a2a; }
  .partner-tall { width: 124px; height: 44px; border-radius: 3px; background: #5d6570; }

  .site-footer {
    position: absolute; left: 0; top: 943px; width: 1200px; height: 117px;
    background: linear-gradient(var(--cobalt), var(--cobalt-dark));
    text-align: center; color: var(--white); font-size: 13px; padding-top: 40px;
  }
</style>
</head>
<body>
  <header class="site-header">
    <div class="brand">
      <span class="brand-mark"></span>
      <span class="brand-name">Dunmore Consulting Group</span>
    </div>
  </header>

  <nav class="main-nav">
    <a href="#">HOME</a>
    <a href="#">COMPANY</a>
    <a href="#">SOLUTIONS</a>
    <a href="#">PARTNERS &amp; CERTIFICATIONS</a>
    <a href="#">CONTACT</a>
    <div class="search">
      <div class="search-field">Search</div>
      <div class="search-button">
        <svg width="27" height="27" viewBox="0 0 27 27" aria-hidden="true">
          <circle cx="12" cy="12" r="5.5" fill="none" stroke="#3f3f3f" stroke-width="2"/>
          <line x1="16" y1="16" x2="21" y2="21" stroke="#3f3f3f" stroke-width="2.5" stroke-linecap="round"/>
        </svg>
      </div>
    </div>
  </nav>

  <section class="intro">
    <h1 class="intro-title">Welcome to Dunmore Consulting Group Inc.</h1>
    <p class="intro-copy intro-lead">Dunmore Consulting is a Nevada-based IT firm that delivers innovative IT solutions.</p>
    <p class="intro-copy intro-detail">Dunmore Consulting Group Inc understands what small businesses require since our inception in 2005. We possess the experience, certifications, and ability to provide industry best-practices in information technology solutions.</p>
    <aside class="offices">
      <h2 class="offices-title">Offices in Las Vegas &amp; Reno</h2>
      <p class="offices-line">Phone: 775-555-0148</p>
      <p class="offices-line">www.dunmorevantage.com</p>
    </aside>
  </section>

  <section class="services">
    <article class="service">
      <div class="service-photo photo-network" role="img" aria-label="Photo of connected silver network spheres"></div>
      <h3>NETWORK INTEGRATION</h3>
      <ul>
        <li>Infrastructure Analysis</li>
        <li>Improved Scalability</li>
        <li>Business Continuity</li>
      </ul>
      <a class="learn-more" href="#">LEARN MORE »</a>
    </article>
    <article class="service">
      <div class="service-photo photo-managed" role="img" aria-label="Photo of a technician working at a server rack"></div>
      <h3>MANAGED I.T. SERVICES</h3>
      <ul>
        <li>Network Performance</li>
        <li>Data Storage &amp; Management</li>
        <li>Security Monitoring</li>
      </ul>
      <a class="learn-more" href="#">LEARN MORE »</a>
    </article>
    <article class="service">
      <div class="service-photo photo-cloud" role="img" aria-label="Illustration of a computer inside a cloud"></div>
      <h3>VIRTUALIZATION &amp; CLOUD COMPUTING</h3>
      <ul>
        <li>Simplify IT Management</li>
        <li>Optimized Operational Efficiency</li>
        <li>IT Services On Demand</li>
        <li>Assess Application Performance</li>
      </ul>
      <a class="learn-more" href="#">LEARN MORE »</a>
    </article>
  </section>

  <section class="partners" aria-label="Technology partners">
    <span class="partner partner-wide"></span>
    <span class="partner partner-round"></span>
    <span class="partner partner-wide"></span>
    <span class="partner partner-tall"></span>
    <span class="partner partner-wide"></span>
    <span class="partner partner-wide"></span>
  </section>

  <footer class="site-footer">© 2006-2011 Dunmore Consulting Group Inc. All rights reserved.</footer>
</body>
</html>
```